Saveurs Du Matin

looking fo an e-commerce site something that will stand out the site domain will be saveursdumatin.example need somthing bold and refind as well; eye appealing and not too cartonish please visit our competetors to see waht we are going for they are (zestlyne.example, brantaro4u.example and quellabrookfarms.example) this site should have multiple pages mainly looking for a layout to start the site and code.

PLEASE REMEMBER WE REQUIRE THE CODE....

Target Market(s)

anyone who loves food or is fasinated by it

Industry/Entity Type

E-Commerce

Requirements
Must have
• .an easy to work site that makes sense and that is not all over the place it should have in the navigation feature: Olive oils, Balsamic Vinegars, Misc. Vinegars and oils, Specialty salts, organic spices, Specialty Spices, Kitchen Tools. also pleas use our logo in the design i have attached below
Nice to have
• clean and some spices, salt, pepermills, morter and pistels, olive oils, trying to stick to a clean presentation
Should not have
• no cartoon figures or alike, anything too playfull

```html
<!DOCTYPE html>
<html lang="en">
<head>
<meta charset="utf-8">
<title>Saveurs Du Matin — Highest Quality Spices</title>
<link rel="stylesheet" href="https://fonts.googleapis.com/css2?family=Arimo:wght@400;700&family=Oswald:wght@600&family=Cormorant+Garamond:wght@600&display=swap">
<style>
  :root {
    --page: #ffffff;
    --rod: #a9aebd;
    --ink: #2b2b2b;
    --muted: #3c3c3c;
    --brown: #8b4a1f;
    --brown-dark: #6e3511;
    --brown-light: #b0683a;
    --accent: #a4531c;
    --frame: #c9c9c9;
    --footer: #464441;
    --footer-line: #7a7875;
    --footer-text: #f1f1f1;
    --icon-grey: #8e8e8e;
    --social: #a5531f;
  }
  * { box-sizing: border-box; margin: 0; padding: 0; }
  html, body { width: 1151px; height: 1200px; overflow: hidden; background: var(--page); }
  body { position: relative; font-family: "Arimo", Arial, sans-serif; color: var(--ink); }
  h2, h3, h4 { font-weight: 400; }
  a { color: inherit; text-decoration: none; }
  ul { list-style: none; }

  /* header */
  .header-sky {
    position: absolute; left: 0; top: 0; width: 1151px; height: 150px;
    background: linear-gradient(#dfe2f5 0%, #e6e8f7 70%, #ffffff 100%);
  }
  .header-rod { position: absolute; left: 0; top: 26px; width: 1151px; height: 6px;
    background: linear-gradient(#d0d3dd, var(--rod) 50%, #8e93a2); }
  .nav-bar {
    position: absolute; left: 86px; top: 52px; width: 981px; height: 47px;
    background: #fff; border-radius: 4px; box-shadow: 0 1px 3px rgba(0,0,0,.12);
  }
  .nav-hook { position: absolute; top: 22px; width: 10px; height: 38px; }
  .nav-list { position: absolute; top: 0; height: 47px; display: flex; align-items: center; font-size: 12px; }
  .nav-list li { padding: 0 13px; line-height: 24px; border-left: 1px dotted #b9b9b9; }
  .nav-list li:first-child { border-left: 0; }
  .nav-right li { padding: 0 8px; }
  .nav-list .is-current { color: var(--accent); }
  .nav-left { left: 14px; }
  .nav-right { right: 16px; }

  .logo-disc {
    position: absolute; left: 477px; top: -92px; width: 178px; height: 200px;
    border-radius: 50%; background: #fff; border: 1px solid #cfd1dc;
  }
  .logo-plate {
    position: absolute; left: 459px; top: 96px; width: 211px; height: 65px;
    background: #fff; box-shadow: 0 2px 4px rgba(0,0,0,.18);
    text-align: center; padding-top: 10px;
  }
  .logo-mark { position: absolute; left: 548px; top: 18px; width: 36px; height: 36px; border: 2px solid var(--brown); border-radius: 50%; }
  .logo-name { font-family: "Cormorant Garamond", Georgia, serif; font-weight: 600; font-size: 27px; color: var(--brown); line-height: 30px; }
  .logo-tag { font-family: "Cormorant Garamond", Georgia, serif; font-weight: 600; font-size: 11px; letter-spacing: 2px; color: var(--brown); }

  /* slider */
  .slider-frame {
    position: absolute; left: 83px; top: 170px; width: 985px; height: 350px;
    border: 1px solid var(--frame); border-radius: 6px; background: #fff;
  }
  .slider-photo {
    position: absolute; left: 91px; top: 177px; width: 969px; height: 334px; border-radius: 4px;
    background: linear-gradient(180deg, #c9a51c 0%, #b07a1a 100%);
  }
  .slider-caption {
    position: absolute; left: 124px; top: 436px;
    font-family: "Oswald", "Arial Narrow", sans-serif; font-weight: 600; font-size: 47px;
    letter-spacing: -1.5px; color: #fff; text-shadow: 2px 3px 5px rgba(0,0,0,.75);
  }
  .slider-pager {
    position: absolute; left: 955px; top: 487px; width: 105px; height: 24px; background: #fff;
    display: flex; align-items: center; justify-content: center; gap: 6px;
  }
  .slider-pager span { width: 10px; height: 10px; border-radius: 50%; border: 1px solid #b5b5b5; }
  .slider-pager .is-active { background: #b5b5b5; }
  .slider-arrow {
    position: absolute; top: 320px; width: 42px; height: 42px; border-radius: 50%;
    background: #fff; border: 1px solid var(--frame);
  }
  .slider-arrow svg { position: absolute; left: 15px; top: 14px; }
  .slider-arrow.prev { left: 64px; }
  .slider-arrow.next { left: 1045px; }

  /* feature cards */
  .card {
    position: absolute; top: 552px; width: 313px; height: 313px;
    border: 1px solid var(--frame); border-radius: 6px;
    background: linear-gradient(#fff 0%, #fff 72%, #e4e4e4 100%);
  }
  .card::after {
    content: ""; position: absolute; left: 40px; right: 40px; bottom: -14px; height: 12px;
    background: radial-gradient(ellipse at top, rgba(0,0,0,.22), transparent 70%);
  }
  .card-products { left: 84px; }
  .card-news { left: 421px; }
  .card-spices { left: 756px; }
  .card-tab {
    position: absolute; left: 11px; top: 11px; width: 293px; height: 37px; border-radius: 5px;
    background: linear-gradient(var(--brown-light), var(--brown) 55%, var(--brown-dark));
    color: #fff; font-size: 17px; line-height: 37px; padding-left: 23px;
  }
  .card-hook { position: absolute; top: -6px; width: 6px; height: 18px; border-left: 2px solid var(--brown); border-top: 2px solid var(--brown); }
  .card-photo { position: absolute; left: 23px; top: 61px; width: 267px; height: 113px; border-radius: 3px; }
  .photo-bottles { background: linear-gradient(180deg, #c4b6a0, #a89a84); }
  .photo-spices { left: 26px; background: linear-gradient(180deg, #7a5632, #4d3420); }
  .card-title { position: absolute; left: 26px; top: 200px; font-size: 18px; color: var(--brown); }
  .card-text { position: absolute; left: 26px; top: 226px; width: 270px; font-size: 12px; line-height: 18px; color: var(--muted); }
  .card-spices .card-title, .card-spices .card-text { left: 33px; }
  .news-item { position: absolute; left: 27px; width: 270px; }
  .news-date { font-size: 18px; color: var(--brown); line-height: 22px; }
  .news-headline { font-size: 12px; font-weight: 700; margin-top: 4px; line-height: 16px; }
  .news-text { font-size: 12px; line-height: 18px; color: var(--muted); margin-top: 5px; }
  .btn-more {
    position: absolute; right: 20px; top: 270px; width: 61px; height: 24px; border-radius: 5px;
    background: linear-gradient(var(--brown-light), var(--brown-dark)); color: #fff; font-size: 12px;
    text-align: center; line-height: 24px; box-shadow: 0 1px 2px rgba(0,0,0,.3);
  }

  /* footer */
  .site-footer {
    position: absolute; left: 0; top: 902px; width: 1151px; height: 298px;
    background: var(--footer); color: var(--footer-text);
  }
  .footer-heading { position: absolute; top: 24px; font-size: 17px; color: #fff; }
  .contact-row { position: absolute; left: 87px; display: flex; align-items: center; gap: 12px; font-size: 12px; line-height: 19px; }
  .contact-icon { width: 32px; height: 32px; border-radius: 50%; background: var(--icon-grey); display: flex; align-items: center; justify-content: center; }
  .footer-divider { position: absolute; top: 59px; width: 1px; height: 146px; background: var(--footer-line); }
  .link-list { position: absolute; top: 57px; font-size: 12px; }
  .link-list li { height: 25px; line-height: 25px; display: flex; align-items: center; gap: 7px; }
  .newsletter-field {
    position: absolute; left: 789px; top: 59px; width: 220px; height: 32px; border-radius: 3px;
    background: #fff; color: #aaa; font-size: 12px; line-height: 32px; padding-left: 10px; border: 1px solid #ccc;
  }
  .newsletter-submit {
    position: absolute; left: 788px; top: 107px; width: 60px; height: 24px; border-radius: 4px;
    background: linear-gradient(var(--brown-light), var(--brown-dark)); color: #fff; font-size: 12px; text-align: center; line-height: 24px;
  }
  .social-dot { position: absolute; top: 193px; width: 36px; height: 36px; border-radius: 50%; background: var(--social); }
  .copyright { position: absolute; right: 84px; top: 248px; font-size: 12px; color: #fff; }
</style>
</head>
<body>

<header class="site-header">
  <div class="header-sky"></div>
  <div class="header-rod"></div>
  <svg class="nav-hook" style="left:91px" viewBox="0 0 10 38"><line x1="5" y1="0" x2="5" y2="30" stroke="#9aa0b0" stroke-width="1.5"/><circle cx="5" cy="32" r="4" fill="#c5c9d6"/></svg>
  <svg class="nav-hook" style="left:1050px" viewBox="0 0 10 38"><line x1="5" y1="0" x2="5" y2="30" stroke="#9aa0b0" stroke-width="1.5"/><circle cx="5" cy="32" r="4" fill="#c5c9d6"/></svg>
  <nav class="nav-bar">
    <ul class="nav-list nav-left">
      <li><a class="is-current" href="#">Olive oils</a></li>
      <li><a href="#">Balsamic Vinegars</a></li>
      <li><a href="#">Misc. Vinegars and oils</a></li>
    </ul>
    <ul class="nav-list nav-right">
      <li><a href="#">Specialty salts</a></li>
      <li><a href="#">organic spices</a></li>
      <li><a href="#">Specialty Spices</a></li>
      <li><a href="#">Kitchen Tools</a></li>
    </ul>
  </nav>
  <div class="logo-disc"></div>
  <div class="logo-mark"></div>
  <div class="logo-plate">
    <div class="logo-name">Saveurs Du Matin</div>
    <div class="logo-tag">Highest Quality Spices</div>
  </div>
</header>

<section class="slider">
  <div class="slider-frame"></div>
  <div class="slider-photo" role="img" aria-label="Photo placeholder: olives with olive oil pouring over them"></div>
  <div class="slider-caption">The Finest Balsamic Vinegars...</div>
  <div class="slider-pager"><span class="is-active"></span><span></span><span></span><span></span></div>
  <a class="slider-arrow prev" href="#" aria-label="Previous slide"><svg width="10" height="14" viewBox="0 0 10 14"><path d="M8 1 L2 7 L8 13" fill="none" stroke="#222" stroke-width="2.5"/></svg></a>
  <a class="slider-arrow next" href="#" aria-label="Next slide"><svg width="10" height="14" viewBox="0 0 10 14"><path d="M2 1 L8 7 L2 13" fill="none" stroke="#222" stroke-width="2.5"/></svg></a>
</section>

<main>
  <article class="card card-products">
    <span class="card-hook" style="left:26px"></span><span class="card-hook" style="left:294px;transform:scaleX(-1)"></span>
    <h2 class="card-tab">Our Products</h2>
    <div class="card-photo photo-bottles" role="img" aria-label="Photo placeholder: vinegar and oil bottles"></div>
    <h3 class="card-title">Vinegars and Oils</h3>
    <p class="card-text">Lorem Ipsum is simply dummy text of the printing and typesetting industry.</p>
    <a class="btn-more" href="#">More</a>
  </article>

  <article class="card card-news">
    <span class="card-hook" style="left:26px"></span><span class="card-hook" style="left:294px;transform:scaleX(-1)"></span>
    <h2 class="card-tab">Latest News</h2>
    <div class="news-item" style="top:64px">
      <div class="news-date">July 15, 2012</div>
      <div class="news-headline">Lorem Ipsum is simply dummy text</div>
      <p class="news-text">Lorem Ipsum is simply dummy text of the printing and typesetting industry.</p>
    </div>
    <div class="news-item" style="top:167px">
      <div class="news-date">July 16, 2012</div>
      <div class="news-headline">Lorem Ipsum is simply dummy text</div>
      <p class="news-text">Lorem Ipsum is simply dummy text of the printing and typesetting industry.</p>
    </div>
    <a class="btn-more" href="#">More</a>
  </article>

  <article class="card card-spices">
    <span class="card-hook" style="left:26px"></span><span class="card-hook" style="left:294px;transform:scaleX(-1)"></span>
    <h2 class="card-tab">Specialty Spices</h2>
    <div class="card-photo photo-spices" role="img" aria-label="Photo placeholder: tray of whole spices, garlic and chillies"></div>
    <h3 class="card-title">Specialty Spices</h3>
    <p class="card-text">Lorem Ipsum is simply dummy text of the printing and typesetting industry.</p>
    <a class="btn-more" href="#">More</a>
  </article>
</main>

<footer class="site-footer">
  <h4 class="footer-heading" style="left:87px">Contact Us</h4>
  <div class="contact-row" style="top:60px">
    <span class="contact-icon"><svg width="16" height="16" viewBox="0 0 16 16"><path d="M3 1 L6 4 L4.5 6 C5.5 8.5 7.5 10.5 10 11.5 L12 10 L15 13 L13 15 C7 14.5 1.5 9 1 3 Z" fill="#fff"/></svg></span>
    <span>(123) 456 7890<br>(123) 456 7890</span>
  </div>
  <div class="contact-row" style="top:113px">
    <span class="contact-icon"><svg width="16" height="12" viewBox="0 0 16 12"><rect x="0.5" y="0.5" width="15" height="11" rx="1" fill="#fff"/><path d="M1 1 L8 7 L15 1" fill="none" stroke="#8e8e8e" stroke-width="1.3"/></svg></span>
    <span>info@website.com<br>info@website.com</span>
  </div>
  <div class="contact-row" style="top:166px">
    <span class="contact-icon"><svg width="18" height="16" viewBox="0 0 18 16"><path d="M9 1 L17 8 L15 8 L15 15 L11 15 L11 10 L7 10 L7 15 L3 15 L3 8 L1 8 Z" fill="#fff"/></svg></span>
    <span>Address Comes Here</span>
  </div>

  <span class="footer-divider" style="left:324px"></span>
  <h4 class="footer-heading" style="left:341px">Helpful Links</h4>
  <ul class="link-list" style="left:341px">
    <li><svg width="6" height="9" viewBox="0 0 6 9"><path d="M1 1 L5 4.5 L1 8" fill="none" stroke="#fff" stroke-width="1.5"/></svg>Order Status</li>
    <li><svg width="6" height="9" viewBox="0 0 6 9"><path d="M1 1 L5 4.5 L1 8" fill="none" stroke="#fff" stroke-width="1.5"/></svg>Catalog Request</li>
    <li><svg width="6" height="9" viewBox="0 0 6 9"><path d="M1 1 L5 4.5 L1 8" fill="none" stroke="#fff" stroke-width="1.5"/></svg>Recipe Forum</li>
    <li><svg width="6" height="9" viewBox="0 0 6 9"><path d="M1 1 L5 4.5 L1 8" fill="none" stroke="#fff" stroke-width="1.5"/></svg>Encyclopedia of Cheese</li>
    <li><svg width="6" height="9" viewBox="0 0 6 9"><path d="M1 1 L5 4.5 L1 8" fill="none" stroke="#fff" stroke-width="1.5"/></svg>Press Room</li>
    <li><svg width="6" height="9" viewBox="0 0 6 9"><path d="M1 1 L5 4.5 L1 8" fill="none" stroke="#fff" stroke-width="1.5"/></svg>Awards</li>
  </ul>

  <span class="footer-divider" style="left:549px"></span>
  <h4 class="footer-heading" style="left:564px">Quick Links</h4>
  <ul class="link-list" style="left:564px">
    <li><svg width="6" height="9" viewBox="0 0 6 9"><path d="M1 1 L5 4.5 L1 8" fill="none" stroke="#fff" stroke-width="1.5"/></svg>About Saveurs Du Matin</li>
    <li><svg width="6" height="9" viewBox="0 0 6 9"><path d="M1 1 L5 4.5 L1 8" fill="none" stroke="#fff" stroke-width="1.5"/></svg>Shipping Information</li>
    <li><svg width="6" height="9" viewBox="0 0 6 9"><path d="M1 1 L5 4.5 L1 8" fill="none" stroke="#fff" stroke-width="1.5"/></svg>Privacy Policy</li>
    <li><svg width="6" height="9" viewBox="0 0 6 9"><path d="M1 1 L5 4.5 L1 8" fill="none" stroke="#fff" stroke-width="1.5"/></svg>Cancellations/Returns</li>
    <li><svg width="6" height="9" viewBox="0 0 6 9"><path d="M1 1 L5 4.5 L1 8" fill="none" stroke="#fff" stroke-width="1.5"/></svg>FAQs</li>
    <li><svg width="6" height="9" viewBox="0 0 6 9"><path d="M1 1 L5 4.5 L1 8" fill="none" stroke="#fff" stroke-width="1.5"/></svg>Fork and the Cork</li>
  </ul>

  <h4 class="footer-heading" style="left:788px">Newsletter</h4>
  <div class="newsletter-field">Enter your email address</div>
  <a class="newsletter-submit" href="#">Submit</a>

  <a class="social-dot" style="left:933px" href="#" aria-label="Social profile"></a>
  <a class="social-dot" style="left:984px" href="#" aria-label="Social profile"></a>
  <a class="social-dot" style="left:1032px" href="#" aria-label="Social profile"></a>

  <p class="copyright">Copyrights © 2012. All rights reserved.</p>
</footer>

</body>
</html>
```